Website re-design

We are a successful furnished apartment provider in Boston. We currently are working on re-designing our website www.ribtenlofts.com to make it more modern, designer look and user friendly. We hired a designer, but are not happy with the designs proposed and want to improve on them. The winning design will be paid regardless of whether we stay with our current designer or not. We want ideas and functional page links to see how it will work. Platform we have chosen is wordpress. Feel free to propose others easy for us to update and modify. We do not like Joomla on which website is currently running. We do not like flash nor long load times.
Please use photos on our website for design presentations. www.ribtenlofts.com

Target Market(s)

doctors, nurses, business men but mostly business women, some post-medical students

Industry/Entity Type

Apartment

Requirements
Must have
• Quick action button for reservation form and a notification and email forwarding system to us of reservation information by potential clients. Blog required with feedback by guests allowed, we can censor which are published. Slide shows of apartments.
Should not have
• No movies.

```html
<!DOCTYPE html>
<html lang="en">
<head>
<meta charset="utf-8">
<title>Ribten Lofts – Furnished Apartments</title>
<link rel="stylesheet" href="https://fonts.googleapis.com/css2?family=Cinzel:wght@500&family=Marcellus&family=Arimo:wght@400;700&display=swap">
<style>
:root{
  --bg:#2c2c2c;
  --bg-dark:#1c1c1c;
  --nav:#171717;
  --gold:#c9a95a;
  --gold-light:#d8bf74;
  --text:#a9a9a9;
  --heading:#dcdcdc;
  --white:#ffffff;
  --rule:#4a4a4a;
}
*{margin:0;padding:0;box-sizing:border-box}
html,body{width:1200px;height:1091px;overflow:hidden}
body{
  background:var(--bg);
  background-image:repeating-linear-gradient(45deg,rgba(255,255,255,.015) 0 2px,transparent 2px 5px);
  font-family:"Arimo",Arial,sans-serif;color:var(--text);position:relative;
}
.top-rule{position:absolute;top:27px;left:0;width:1200px;height:1px;background:var(--gold);opacity:.8}
.top-links{position:absolute;top:18px;left:862px;padding:0 8px;background:var(--bg);font-size:13.5px;color:var(--gold-light);display:flex;gap:12px}
.top-links .sep{color:var(--gold)}
.brand{position:absolute;top:45px;left:436px;display:flex;align-items:center;gap:8px}
.brand-mark{width:74px;height:74px;border-radius:50%;background:radial-gradient(circle at 40% 35%,#e3c873,#a98a3c)}
.brand-name{font-family:"Cinzel",serif;font-weight:500;font-size:40px;color:var(--gold);line-height:1}
.brand-sub{position:absolute;top:55px;left:86px;font-family:"Arimo",sans-serif;font-size:11.5px;letter-spacing:6.2px;color:var(--gold)}
.social{position:absolute;top:66px;left:966px;display:flex;gap:14px}
.social a{display:flex;flex-direction:column;align-items:center;text-decoration:none;font-size:9px;color:#8a8a8a;width:38px}
.social .dot{width:26px;height:26px;border-radius:50%;background:#1e1e1e;border:1px solid #3b3b3b;margin-bottom:4px}
.main-nav{position:absolute;top:147px;left:147px;width:905px;height:38px;background:var(--nav);box-shadow:0 3px 6px rgba(0,0,0,.4);display:flex;align-items:center;padding-left:1px}
.main-nav a{font-family:"Marcellus",serif;font-size:15.5px;color:var(--white);text-decoration:none;padding:0 15px;border-right:1px solid #333;line-height:20px}
.main-nav a:last-child{border-right:0}
.main-nav a.active{color:var(--gold);font-weight:bold}
.slider{position:absolute;top:205px;left:147px;width:905px;height:461px;background:var(--bg-dark);box-shadow:0 2px 6px rgba(0,0,0,.5)}
.slide-photo{position:absolute;top:22px;left:21px;width:864px;height:418px;
  background:radial-gradient(ellipse at 75% 35%,#d6c189 0%,#9a8250 35%,transparent 60%),
  linear-gradient(180deg,#8d7a55 0%,#6b5534 45%,#3b2a1c 100%)}
.caption{position:absolute;left:21px;top:343px;width:563px;height:97px;background:rgba(20,16,12,.55);padding:26px 11px 0;font-family:"Marcellus",serif;font-size:23px;line-height:26px;color:var(--white)}
.arrow{position:absolute;top:195px;width:37px;height:46px;background:#111;display:flex;align-items:center;justify-content:center}
.arrow.prev{left:21px}
.arrow.next{left:847px}
.column{position:absolute;top:716px}
.column h2{font-family:"Marcellus",serif;font-weight:400;font-size:29px;color:var(--heading);margin-bottom:17px;line-height:32px}
.column p{font-size:11.5px;line-height:17.3px}
.welcome{left:149px;width:285px}
.services{left:455px;width:280px}
.clients{left:764px;width:285px}
.services ul{list-style:none;margin-top:21px}
.services li{font-size:11.5px;line-height:23px;color:var(--gold-light);padding-left:26px;position:relative}
.services li::before{content:"";position:absolute;left:2px;top:8px;width:6px;height:6px;background:var(--gold)}
.services li.wrap{line-height:24px}
.clients strong{color:var(--white)}
.clients p+p{margin-top:17px}
.btn{position:absolute;top:952px;width:81px;height:27px;background:#151515;border:1px solid #222;color:var(--white);font-size:12.5px;display:flex;align-items:center;justify-content:center;text-decoration:none}
.btn.services-more{left:458px}
.btn.clients-more{left:766px}
.footer-rule{position:absolute;top:1041px;left:152px;width:900px;height:1px;background:var(--rule)}
.copyright{position:absolute;top:1059px;left:152px;width:900px;text-align:center;font-size:12px;color:var(--text)}
</style>
</head>
<body>
<div class="top-rule"></div>
<nav class="top-links"><span>Links</span><span class="sep">|</span><span>Chirpline</span><span class="sep">|</span><span>Boston</span></nav>

<header class="brand">
  <div class="brand-mark"></div>
  <div class="brand-name">RIBTEN LOFTS</div>
  <div class="brand-sub">FURNISHED APARTMENTS</div>
</header>

<div class="social">
  <a href="#"><span class="dot"></span>Chirpline</a>
  <a href="#"><span class="dot"></span>friendbook</a>
</div>

<nav class="main-nav">
  <a class="active" href="#">HOME</a>
  <a href="#">CONTACT</a>
  <a href="#">APARTMENTS</a>
  <a href="#">RESERVATIONS</a>
  <a href="#">LOCATIONS</a>
  <a href="#">RATES</a>
  <a href="#">BLOG</a>
  <a href="#">REVIEWS</a>
  <a href="#">ABOUT US</a>
</nav>

<section class="slider">
  <div class="slide-photo" role="img" aria-label="Photo of a furnished bedroom with a double bed, armchairs, a rug and tall curtained windows"></div>
  <div class="caption">Ribten Lofts is proud to offer some of the best furnished apartments in Boston</div>
  <a class="arrow prev" href="#" aria-label="Previous slide"><svg width="12" height="14" viewBox="0 0 12 14"><path d="M8 2 3 7l5 5" stroke="#fff" stroke-width="2.4" fill="none"/></svg></a>
  <a class="arrow next" href="#" aria-label="Next slide"><svg width="12" height="14" viewBox="0 0 12 14"><path d="M4 2l5 5-5 5" stroke="#fff" stroke-width="2.4" fill="none"/></svg></a>
</section>

<section class="column welcome">
  <h2>WELCOME</h2>
  <p>Ribten Lofts is proud to offer some of the best furnished apartments in Boston. Our locations are in the trendiest area of the city: the South End. In the South End neighborhood, you will find wonderful restaurants, theaters, cafes and artist lofts. Our short term and extended stay apartments are very, very clean. We also offer the latest designer layouts: hardwood floors, Wireless Dsl, Cable TV, flat screen in most apartments, washer and dryer, cookware, cotton linens. Please click links on left for photo galleries, pricing, availability and reservation form and write us for more information. Thank you.</p>
  <p style="margin-top:18px">If you are on Friendbook, please "like" us!</p>
</section>

<section class="column services">
  <h2>SERVICES</h2>
  <p>Lorem Ipsum is simply dummy text of the printing and typesetting industry.</p>
  <ul>
    <li>Lorem Ipsum is simply dummy</li>
    <li>Lorem Ipsum is simply dummy text</li>
    <li>Contrary to popular belief</li>
    <li class="wrap">It is a long established fact that a reader will be distracted</li>
  </ul>
</section>
<a class="btn services-more" href="#">Read more</a>

<section class="column clients">
  <h2>CLIENTS SAY</h2>
  <p><strong>It is a long established fact that a reader</strong> will be distracted by the readable content of a page when looking at its layout.content of a page when looking at its layout.</p>
  <p><strong>It is a long established fact that a reader</strong> will be distracted by the readable content of a page when looking at its layout.content of a page when looking at its layout.</p>
</section>
<a class="btn clients-more" href="#">Read more</a>

<div class="footer-rule"></div>
<footer class="copyright">© RIBTEN LOFTS 2010 - ALL RIGHTS RESERVED</footer>
</body>
</html>
```